A new healing and spiritual podcast needs a design.

We need a design for the podcast that will also be used on the supporting website. The name is Still Lantern Path. The podcast will be about tapping into our own guidance to have a great life. There will be interviews, meditations, discussions on all aspects of energy healing and alternative healing techniques. The website will be where classes will be offered. Looking for something that conveys a peaceful feeling without looking too "healy-feely". Yet also want it to get peoples attention.

Target Market(s)

Metaphysical, spiritual (not religious), energy healers

Font styles to use
Serif

Requirements
Must have
• The name "Still Lantern Path"
Nice to have
• I'd like it to be inviting, catch peoples eye, convey a peaceful feeling, yet not be boring.
Should not have
• Animated (like comic strip) images.

```html
<!DOCTYPE html>
<html lang="en">
<head>
<meta charset="utf-8">
<title>Still Lantern Path Podcast</title>
<link href="https://fonts.googleapis.com/css2?family=Montserrat:wght@500;800&family=Oswald:wght@600&display=swap" rel="stylesheet">
<style>
  :root {
    --night: #21111a;
    --sky-top: #b9837e;
    --sky-glow: #fbd9a8;
    --sky-warm: #f3b27f;
    --ground: #3a2526;
    --white: #ffffff;
    --sand-top: #5a3b2c;
    --sand-bottom: #e6b07c;
    --gold-top: #4a3518;
    --gold-bottom: #e3c000;
    --label: #d8d2d6;
  }
  html, body {
    margin: 0;
    padding: 0;
    width: 1200px;
    height: 1200px;
    overflow: hidden;
    background: var(--night);
  }
  .cover {
    position: relative;
    width: 1200px;
    height: 1200px;
    background: var(--night);
  }
  .cover-art {
    position: absolute;
    inset: 0;
    display: block;
  }
  .title-top {
    font-family: "Montserrat", sans-serif;
    font-weight: 800;
  }
  .title-condensed {
    font-family: "Oswald", sans-serif;
    font-weight: 600;
  }
  .podcast-label {
    position: absolute;
    left: 0;
    right: 0;
    top: 1086px;
    text-align: center;
    font-family: "Montserrat", sans-serif;
    font-weight: 500;
    font-size: 25px;
    letter-spacing: 17px;
    padding-left: 17px;
    color: var(--label);
    margin: 0;
  }
</style>
</head>
<body>
<main class="cover">
  <svg class="cover-art" width="1200" height="1200" viewBox="0 0 1200 1200" xmlns="http://www.w3.org/2000/svg">
    <defs>
      <linearGradient id="skyFade" x1="0" y1="0" x2="0" y2="1">
        <stop offset="0" stop-color="var(--sky-top)"/>
        <stop offset="0.3" stop-color="var(--sky-warm)"/>
        <stop offset="0.55" stop-color="var(--sky-glow)"/>
        <stop offset="0.72" stop-color="var(--sky-warm)"/>
        <stop offset="0.88" stop-color="var(--ground)"/>
        <stop offset="1" stop-color="var(--night)"/>
      </linearGradient>
      <radialGradient id="sunGlow" cx="0.6" cy="0.55" r="0.45">
        <stop offset="0" stop-color="#fff1cf" stop-opacity="0.75"/>
        <stop offset="1" stop-color="#fff1cf" stop-opacity="0"/>
      </radialGradient>
      <linearGradient id="sandText" x1="0" y1="0" x2="0" y2="1">
        <stop offset="0" stop-color="var(--sand-top)"/>
        <stop offset="1" stop-color="var(--sand-bottom)"/>
      </linearGradient>
      <linearGradient id="goldText" x1="0" y1="0" x2="0" y2="1">
        <stop offset="0" stop-color="var(--gold-top)"/>
        <stop offset="1" stop-color="var(--gold-bottom)"/>
      </linearGradient>
    </defs>

    <g class="hero-photo" role="img" aria-label="Photo: silhouette of a person with raised arms against a glowing sunset sky above a city skyline and grassy hill">
      <rect x="0" y="0" width="1200" height="808" fill="url(#skyFade)"/>
      <rect x="0" y="0" width="1200" height="808" fill="url(#sunGlow)"/>
    </g>

    <text class="title-top" x="603" y="692" font-size="208" text-anchor="middle"
          textLength="490" lengthAdjust="spacingAndGlyphs" fill="var(--white)" fill-opacity="0.95">STILL</text>
    <text class="title-condensed" x="603" y="855" font-size="176" text-anchor="middle"
          textLength="620" lengthAdjust="spacingAndGlyphs" fill="url(#sandText)">LANTERN</text>
    <text class="title-condensed" x="603" y="1003" font-size="176" text-anchor="middle"
          textLength="630" lengthAdjust="spacingAndGlyphs" fill="url(#goldText)">PATH</text>
  </svg>
  <p class="podcast-label">PODCAST</p>
</main>
</body>
</html>
```